Design a Website Mockup for Aurevia

This contest is only for Design. The design should be at least 3 pages.
1, Home Page. - Big picture banners
2, Product page
3, Customization page.

Our website will feature 3 main categories:
1, Luxury Range - High end.
2, Luxury - Colorful diamond range
3, Luxury - Custom made.

[url removed, login to view] (our website) - if the link is broken please try and type it into the browser.

***Specialising in Aurevia***
24Kt gold zentrals. Crocodile skin. Diamond phones. High end Aurevia. Custom made Aurevia.
24Kt gold, snake skin, crocodile leather, encrusted in diamonds and belmarodi crystals.

Please see these 3 website as references:-
[url removed, login to view] - (my website) - if the link is broken please try and type it into the browser.

These phones will be of HIGH value and will be sold to the Rich and famous A class [url removed, login to view] will be the most sough after Aurevia for the rich and famous who want to feel special and unique in owning a Luxury Phone.

The Mock up Design of this website must smell LUXURY, see LUXURY, feel LUXURY & DANCE LUXURY in every way possible. having the absolute WOW factor is essential.

The design of the website should be unique in every way and MUST be WOWWW.

Can include but not limited to:-
Sexy Girls
Fast cars
Yachts
Jets

These could be included with the design.

Website must Include a hint of purple - as it show rich and royalty.
The colours Gold, Black, Purple and Silver are Luxury Colours and could tie in with the design.

Please see these website as references:-

[url removed, login to view] - (my website)

The winner of the competition could go on to fully design and develop the website in full. Excellent experience and Excellent communication is essential! Any questions please ask me at any time and i will be looking at the new designs day by day.

```html
<!DOCTYPE html>
<html lang="en">
<head>
<meta charset="utf-8">
<title>Aurevia — Define Luxury</title>
<link href="https://fonts.googleapis.com/css2?family=Playfair+Display:wght@400;700&family=Montserrat:wght@400;600;700&family=Open+Sans:wght@400&family=Raleway:wght@300;700&family=Libre+Baskerville&display=swap" rel="stylesheet">
<style>
:root{
  --gold:#d4a43a;
  --gold-soft:#e2bd5f;
  --white:#ffffff;
  --text-light:#d9d7de;
  --text-muted:#9b9aa3;
  --hero-top:#2c2834;
  --hero-bottom:#1c1a22;
  --feature-bg:#2b2a36;
  --black:#08080a;
  --charcoal:#1f1f24;
  --footer-bg:#2a2a33;
  --line:#d8d8d8;
}
*{box-sizing:border-box;margin:0;padding:0}
html,body{width:1200px;height:3733px;overflow:hidden;background:var(--black)}
body{position:relative;font-family:'Open Sans',sans-serif;color:var(--white)}
section,footer{position:absolute;left:0;width:1200px;overflow:hidden}
.abs{position:absolute}
.photo{position:absolute}

/* brand */
.brand{position:absolute;display:flex;flex-direction:column;align-items:center;gap:10px}
.brand-mark{width:44px;height:44px;border:2px solid var(--gold)}
.brand-name{font-family:'Playfair Display',serif;font-weight:400;font-size:22px;letter-spacing:3px;color:var(--gold)}

/* hero */
.hero{top:0;height:623px;background:radial-gradient(ellipse at 30% 80%,#4a2f3a 0%,transparent 55%),linear-gradient(180deg,var(--hero-top),var(--hero-bottom))}
.nav{position:absolute;top:62px;left:656px;display:flex;gap:18px;font-family:'Libre Baskerville',serif;font-size:12px;color:var(--text-light)}
.nav .active{color:var(--gold)}
.nav .sep{color:var(--text-muted)}
.social{position:absolute;display:flex;gap:10px}
.social span{width:32px;height:32px;border:1.5px solid var(--text-light);border-radius:50%}
.social span.on{border-color:var(--gold)}
.hero-title{left:91px;top:248px;font-family:'Playfair Display',serif;font-size:46px;letter-spacing:1px;color:var(--white);font-weight:400}
.hero-title b{color:var(--gold);font-weight:700}
.hero-copy{left:91px;top:320px;width:500px;font-size:17px;line-height:28px;color:var(--text-light)}
.btn-outline{left:90px;top:406px;width:176px;height:55px;border:1.5px solid var(--text-light);display:flex;align-items:center;justify-content:center;font-family:'Montserrat',sans-serif;font-weight:700;font-size:15px;letter-spacing:1px;color:var(--gold)}

/* features */
.features{top:623px;height:802px;background:radial-gradient(ellipse at 85% 30%,#4a2b3e 0%,transparent 50%),var(--feature-bg)}
.features-title{width:100%;top:50px;text-align:center;font-family:'Raleway',sans-serif;font-weight:300;font-size:32px;color:var(--white)}
.features-title b{font-weight:700}
.feature-label{font-family:'Raleway',sans-serif;font-size:16px;line-height:29px;color:var(--text-light)}
.feature-label.right{text-align:right}
.swatch{position:absolute;width:110px;height:110px;border-radius:50%;border:4px solid var(--white)}

/* category bands */
.category-title{font-family:'Montserrat',sans-serif;font-weight:700;font-size:30px;letter-spacing:5px;line-height:52px}
.category-copy{font-family:'Montserrat',sans-serif;font-size:14px;line-height:26px;color:var(--text-light)}
.link-arrow{font-family:'Montserrat',sans-serif;font-weight:700;font-size:15px;letter-spacing:1px}
.pager{position:absolute;display:flex;flex-direction:column;gap:7px}
.pager i{display:block;width:11px;height:11px;border:2px solid var(--white)}
.pager i.on{background:var(--gold);border-color:var(--gold);height:13px}

.range-high{top:1425px;height:553px;background:var(--black)}
.range-color{top:1978px;height:555px;background:var(--charcoal)}
.range-custom{top:2533px;height:561px;background:var(--black)}

/* gallery */
.gallery{top:3094px;height:403px;background:var(--white)}
.tile{position:absolute;top:11px;height:377px}
.handle{position:absolute;left:0;right:0;bottom:0;height:48px;background:rgba(20,20,24,.55);display:flex;align-items:center;gap:14px;padding-left:22px;font-family:'Montserrat',sans-serif;font-size:14px;color:var(--white)}
.handle i{width:30px;height:22px;border:1.5px solid var(--white)}

/* footer */
.site-footer{top:3497px;height:236px;background:var(--footer-bg)}
.copyright{left:88px;top:184px;font-size:13px;color:var(--text-light)}
</style>
</head>
<body>

<section class="hero">
  <div class="brand" style="left:104px;top:26px">
    <div class="brand-mark"></div>
    <div class="brand-name">AUREVIA</div>
  </div>
  <nav class="nav">
    <span class="active">Home</span><span class="sep">|</span>
    <span>Products</span><span class="sep">|</span>
    <span>Customization</span>
  </nav>
  <div class="social" style="left:953px;top:56px"><span></span><span class="on"></span><span></span><span></span></div>

  <h1 class="abs hero-title">DEFINE <b>LUXURY</b></h1>
  <p class="abs hero-copy">It was popularised in the 1960s with the release of Letraset sheets containing Lorem Ipsum passages</p>
  <div class="abs btn-outline">CONTACT US →</div>

  <div class="photo" role="img" aria-label="Gold zentrals phone with crystal-studded frame, shown at an angle"
       style="left:640px;top:190px;width:480px;height:330px;border-radius:40px;transform:rotate(24deg);background:linear-gradient(135deg,#f6df9a,#c9963a 55%,#8a6222)"></div>
</section>

<section class="features">
  <h2 class="abs features-title">Lorem Ipsum is <b>Simply Dummy</b></h2>

  <div class="photo" role="img" aria-label="Gold zentrals phone seen from the back"
       style="left:503px;top:157px;width:193px;height:391px;border-radius:28px;background:linear-gradient(180deg,#f5e1ad,#d9b56d 60%,#c99f55)"></div>

  <svg class="abs" style="left:0;top:0" width="1200" height="802" aria-hidden="true">
    <g stroke="var(--line)" stroke-width="1.5" fill="none">
      <line x1="394" y1="264" x2="598" y2="264"/>
      <line x1="659" y1="212" x2="800" y2="212"/>
      <line x1="394" y1="478" x2="558" y2="478"/>
      <polyline points="810,478 674,478 674,525"/>
    </g>
    <g fill="var(--white)">
      <circle cx="598" cy="264" r="3"/><circle cx="659" cy="212" r="3"/>
      <circle cx="558" cy="478" r="3"/><circle cx="674" cy="525" r="3"/>
    </g>
  </svg>

  <div class="swatch" role="img" aria-label="Close-up of belmarodi crystals" style="left:284px;top:209px;background:radial-gradient(circle,#e8e8ea,#7d7d82)"></div>
  <div class="swatch" role="img" aria-label="Close-up of 24Kt gold detailing" style="left:800px;top:155px;background:radial-gradient(circle,#e9c66b,#6a4a18)"></div>
  <div class="swatch" role="img" aria-label="Close-up of crocodile skin leather" style="left:284px;top:423px;background:radial-gradient(circle,#d78a5a,#9a4f2b)"></div>
  <div class="swatch" role="img" aria-label="Close-up of diamond-set phone edge" style="left:810px;top:423px;background:radial-gradient(circle,#f0d38a,#8a6a2a)"></div>

  <p class="abs feature-label right" style="right:933px;top:239px">Belmarodi<br>Crystals</p>
  <p class="abs feature-label" style="left:927px;top:196px">24Kt Gold</p>
  <p class="abs feature-label right" style="right:933px;top:452px">Crocodile<br>Skin</p>
  <p class="abs feature-label" style="left:932px;top:452px">Diamond<br>Phone</p>

  <div class="photo" role="img" aria-label="Gold zentrals phone lying flat with crystal-studded sides"
       style="left:290px;top:609px;width:620px;height:137px;border-radius:40px;background:linear-gradient(180deg,#f2c55a,#d59a2a 60%,#b07a1e)"></div>
</section>

<section class="range-high">
  <div class="photo" role="img" aria-label="Dark blue phone in a silver metal bumper, close-up"
       style="left:0;top:0;width:770px;height:553px;background:radial-gradient(ellipse at 45% 40%,#2b3550 0%,#151a28 45%,var(--black) 80%)"></div>
  <div class="pager" style="left:50px;top:238px"><i></i><i></i><i></i><i class="on"></i></div>
  <h2 class="abs category-title" style="left:713px;top:155px;color:var(--white)">LUXURY RANGE -<br>HIGH END</h2>
  <p class="abs category-copy" style="left:713px;top:273px">Lorem Ipsum is simply dummy text of the</p>
  <p class="abs link-arrow" style="left:715px;top:348px;color:var(--gold)">CONTACT US →</p>
</section>

<section class="range-color">
  <div class="photo" role="img" aria-label="Phone with blue glitter diamond case"
       style="left:420px;top:0;width:667px;height:555px;background:radial-gradient(ellipse at 55% 50%,#2aa8d4 0%,#1a6f9a 40%,var(--charcoal) 75%)"></div>
  <h2 class="abs category-title" style="left:91px;top:155px;color:var(--white);line-height:44px">COLORFUL DIAMOND<br>RANGE</h2>
  <p class="abs link-arrow" style="left:91px;top:330px;color:var(--white)">CONTACT US →</p>
  <div class="pager" style="left:1133px;top:243px"><i></i><i></i><i></i><i class="on"></i></div>
</section>

<section class="range-custom">
  <div class="photo" role="img" aria-label="Black snakeskin phone case with gold monogram initials"
       style="left:0;top:0;width:754px;height:561px;background:linear-gradient(90deg,#2a2c30 0%,#1a1b1e 55%,var(--black) 100%)"></div>
  <div class="pager" style="left:50px;top:244px"><i></i><i></i><i></i><i class="on"></i></div>
  <h2 class="abs category-title" style="left:632px;top:175px;color:var(--gold)">LUXURY - CUSTOM<br>MADE</h2>
  <p class="abs category-copy" style="left:632px;top:291px;width:490px;color:var(--text-muted)">Lorem Ipsum is simply dummy text of the printing and typesetting industry. Lorem Ipsum has been the industry's standard dummy text ever since the 1500s.....</p>
</section>

<section class="gallery">
  <div class="tile" role="img" aria-label="Pink phone case with white floral lace pattern" style="left:0;width:203px;background:linear-gradient(135deg,#e6b9b6,#c98f8c)"></div>
  <div class="tile" role="img" aria-label="Rose gold faceted crystal phone case" style="left:217px;width:374px;background:linear-gradient(135deg,#f3d0c8,#d99c92 60%,#8f6a66)">
    <div class="handle"><i></i>@velvet_atelier</div>
  </div>
  <div class="tile" role="img" aria-label="Black crocodile leather phone case with gold emblem" style="left:607px;width:377px;background:linear-gradient(135deg,#3a3a3e,#141416)"></div>
  <div class="tile" role="img" aria-label="Phone back covered in gold mosaic crystals" style="left:997px;width:203px;background:linear-gradient(135deg,#1c1a18,#8a6b4a 60%,#b8916a)"></div>
</section>

<footer class="site-footer">
  <div class="brand" style="left:555px;top:38px">
    <div class="brand-mark"></div>
    <div class="brand-name">AUREVIA</div>
  </div>
  <p class="abs copyright">Copyright 2017. All Right Reserved</p>
  <div class="social" style="left:953px;top:176px"><span></span><span></span><span></span><span></span></div>
</footer>

</body>
</html>
```